Business Card Design Project

Looking for a logo and business card for a Real State Business i will be opening. The name is not choosen yet , but will probably be RKT IMOVEIS.
I was thinking black and silver colors, but am open to nice ideas.
I did add a business card that i liked a lot, am looking for something like that, with logo in black or silver in a black card. The logo i was thinking in the letters RKT as i uploaded or something or little and cute buildings or a house...just ideas, can be any nice logo.
Updates

You guys can add other colors if you want, I like colors very "BRIGHT" and "open", like red, pink, strong colors. almost glow in the dark colors. lol

Designers,

I've increased more 88 dollars in the budget for 1st place cause I will want envelope designs... small and big sizes.

So 1st place is now U$248,00. 

No need to send the envelope designs right now... only the business cards designs.

Thank you.

Industry/Entity Type

Business

Requirements
Must have
• Patricia Souza Ramos

www.RKTimoveisx.com.br

+554193817462

patricia@rktimoveisx.com.br

```html
<!DOCTYPE html>
<html lang="pt-BR">
<head>
<meta charset="utf-8">
<title>RKT Imoveis – Cartão de visita</title>
<link rel="stylesheet" href="https://fonts.googleapis.com/css2?family=Exo+2:wght@400;600;700&display=swap">
<style>
  :root {
    --page-bg: #ffffff;
    --card-bg: #231f20;
    --skyline: #000000;
    --accent-blue: #29abe2;
    --text-white: #ffffff;
    --card-shadow: rgba(0, 0, 0, 0.35);
  }
  * { margin: 0; padding: 0; box-sizing: border-box; }
  html, body {
    width: 1200px;
    height: 900px;
    overflow: hidden;
    background: var(--page-bg);
    font-family: "Exo 2", sans-serif;
  }
  .stage {
    position: relative;
    width: 1200px;
    height: 900px;
  }
  .card {
    position: absolute;
    left: 404px;
    width: 393px;
    height: 234px;
    background: var(--card-bg);
    box-shadow: 4px 6px 14px var(--card-shadow);
    overflow: hidden;
  }
  .card--front { top: 209px; }
  .card--back  { top: 457px; }

  .brand {
    position: absolute;
    display: flex;
    align-items: center;
    gap: 8px;
    transform: translate(-50%, -50%);
    color: var(--text-white);
    font-weight: 700;
    letter-spacing: 0.04em;
    line-height: 1;
  }
  .brand__square {
    background: var(--accent-blue);
  }
  .card--front .brand {
    left: 196px;
    top: 44px;
    font-size: 40px;
  }
  .card--front .brand__square { width: 14px; height: 14px; }

  .holder-name {
    position: absolute;
    left: 14px;
    top: 158px;
    width: 156px;
    text-align: center;
    color: var(--text-white);
    font-size: 20px;
    font-weight: 600;
    line-height: 27px;
  }
  .contact {
    position: absolute;
    left: 199px;
    top: 153px;
    list-style: none;
    color: var(--accent-blue);
    font-size: 14px;
    line-height: 20.5px;
  }

  .skyline {
    position: absolute;
    left: 0;
    bottom: 0;
    width: 100%;
    height: 94px;
    background: linear-gradient(to bottom, #0a0a0a, var(--skyline));
  }
  .card--back .brand {
    left: 195px;
    top: 112px;
    font-size: 84px;
    gap: 14px;
  }
  .card--back .brand__square { width: 26px; height: 26px; }
</style>
</head>
<body>
<main class="stage">
  <section class="card card--front" aria-label="Frente do cartão">
    <div class="brand">
      <span class="brand__square" aria-hidden="true"></span>
      <span class="brand__name">RKT</span>
    </div>
    <p class="holder-name">Patricia Souza<br>Ramos</p>
    <ul class="contact">
      <li>www.RKTimoveisx.com.br</li>
      <li>+554193817462</li>
      <li>patricia@rktimoveisx.com.br</li>
    </ul>
  </section>

  <section class="card card--back" aria-label="Verso do cartão">
    <div class="skyline" role="img" aria-label="Silhueta de prédios da cidade em preto"></div>
    <div class="brand">
      <span class="brand__square" aria-hidden="true"></span>
      <span class="brand__name">RKT</span>
    </div>
  </section>
</main>
</body>
</html>
```